Corporate flyer introducing a brand new technology apprenticeship program in Australia!

A professional, yet clean and contemporary looking flyer to advertise a brand new service offering in a simple, easy to read format with engaging images. Here is a link to our current online brochure which outlines the program we would like to advertise in a hardcopy flyer/brochure format: https://pages.vendrap.com/Information-on-Technology-Higher-Apprenticeships-for-Employers-Victoria-kT3pzqW7LmRe

Target Market(s)

Medium to large sized businesses involved in using cutting edge technology, such as engineering and advanced manufracturing (3D printing etc)

Industry/Entity Type

Engineering

Colors

Designer to choose colors to be used in the design.

Requirements
Must have
• Contemporary, clean looking, easy to read, tech/engineering/advanced manufacturing related imagery
Nice to have
• Some ideas about different sizes/styles (eg something other than a plain A4 sheet)
Should not have
• Unprofessional or offensive language

```html
<!DOCTYPE html>
<html lang="en">
<head>
<meta charset="utf-8">
<title>Technology Higher Apprentices – Brochure</title>
<link href="https://fonts.googleapis.com/css2?family=Archivo:wght@400;500;700;800&display=swap" rel="stylesheet">
<style>
  :root {
    --backdrop: #e4e0df;
    --paper: #ffffff;
    --brand-red: #d32336;
    --brand-red-deep: #a8142a;
    --brand-orange: #ef5a24;
    --ink: #2b2b2b;
    --ink-soft: #555555;
    --map-grey: #e6e6e6;
  }
  * { box-sizing: border-box; margin: 0; padding: 0; }
  html, body { width: 1200px; height: 800px; overflow: hidden; }
  body {
    background: var(--backdrop);
    font-family: "Archivo", Arial, sans-serif;
    position: relative;
  }

  .page {
    position: absolute;
    top: 220px;
    width: 360px;
    height: 360px;
    background: var(--paper);
    box-shadow: 0 6px 18px rgba(0,0,0,.12);
    overflow: hidden;
  }

  /* ---------- Cover ---------- */
  .cover { left: 40px; }
  .cover-frame {
    position: absolute; inset: 10px;
    border: 1px solid var(--brand-orange);
  }
  .cover-photo { position: absolute; inset: 0; }
  .brand-lockup {
    position: absolute; top: 28px; left: 22px;
    display: flex; align-items: center; gap: 10px;
    color: #fff;
  }
  .brand-mark { width: 12px; height: 12px; background: #fff; }
  .brand-name { font-weight: 700; font-size: 15px; letter-spacing: .02em; }
  .brand-divider { width: 1px; height: 32px; background: rgba(255,255,255,.8); }
  .brand-sub { font-size: 11px; line-height: 1.05; font-weight: 500; }
  .brand-sub small { display: block; font-size: 5.5px; letter-spacing: .08em; margin-top: 2px; }
  .cover-title {
    position: absolute; left: 24px; bottom: 30px;
    color: #fff; font-weight: 800; font-size: 22px; line-height: 1.05;
    letter-spacing: .02em; text-transform: uppercase;
  }

  /* ---------- Inside left ---------- */
  .inside-left { left: 440px; box-shadow: none; }
  .inside-right { left: 800px; box-shadow: none; }
  .spread-shadow {
    position: absolute; top: 220px; left: 440px; width: 720px; height: 360px;
    box-shadow: 0 6px 18px rgba(0,0,0,.12);
  }
  .inside-photo { position: absolute; inset: 0; }
  .inside-headline {
    position: absolute; top: 26px; left: 24px; right: 24px;
    color: #fff; font-weight: 800; font-size: 21px; line-height: 1.08;
    text-transform: uppercase; letter-spacing: .02em;
  }

  /* ---------- Inside right ---------- */
  .inside-frame {
    position: absolute; inset: 12px;
    border: 1px solid var(--brand-orange);
  }
  .map-area { position: absolute; right: 22px; top: 80px; width: 170px; height: 170px; }
  .units {
    position: absolute; top: 26px; left: 26px; width: 250px;
  }
  .units-heading {
    font-size: 8px; font-weight: 800; color: var(--ink);
    letter-spacing: .05em; margin-bottom: 4px;
  }
  .level-band {
    display: inline-block;
    background: var(--brand-orange); color: #fff;
    font-size: 8px; font-weight: 700;
    padding: 3px 12px 3px 6px; margin: 3px 0 4px;
  }
  .unit-list { list-style: none; margin-bottom: 6px; }
  .unit-list li {
    font-size: 7px; line-height: 9.6px; color: var(--ink-soft);
  }
</style>
</head>
<body>

  <!-- Cover -->
  <section class="page cover">
    <div class="cover-frame"></div>
    <svg class="cover-photo" viewBox="0 0 360 360" role="img" aria-label="Photograph of a person working on a laptop, tinted red">
      <defs>
        <linearGradient id="coverTint" x1="0" y1="0" x2="1" y2="1">
          <stop offset="0" stop-color="#e03040"/>
          <stop offset="1" stop-color="#b5182c"/>
        </linearGradient>
      </defs>
      <polygon points="0,0 290,24 345,208 275,360 0,360" fill="url(#coverTint)"/>
    </svg>
    <div class="brand-lockup">
      <span class="brand-mark"></span>
      <span class="brand-name">MERIDIAN</span>
      <span class="brand-divider"></span>
      <span class="brand-sub">SKILLS<br>PATHWAYS<small>WORKFORCE PROGRAMS</small></span>
    </div>
    <h1 class="cover-title">Technology<br>Higher<br>Apprentices</h1>
  </section>

  <!-- Inside spread -->
  <div class="spread-shadow"></div>
  <section class="page inside-left">
    <svg class="inside-photo" viewBox="0 0 360 360" role="img" aria-label="Photograph of apprentices working on engineering equipment, tinted red">
      <defs>
        <linearGradient id="insideTint" x1="0" y1="0" x2="1" y2="1">
          <stop offset="0" stop-color="#d9293b"/>
          <stop offset="1" stop-color="#a8142a"/>
        </linearGradient>
      </defs>
      <rect width="360" height="360" fill="url(#insideTint)"/>
    </svg>
    <h2 class="inside-headline">Experience both on<br>and off-the-job<br>training like never<br>before.</h2>
  </section>

  <section class="page inside-right">
    <div class="inside-frame"></div>
    <svg class="map-area" viewBox="0 0 170 170" role="img" aria-label="Map of Australia">
      <rect x="10" y="20" width="150" height="130" rx="40" fill="var(--map-grey)"/>
    </svg>
    <div class="units">
      <h3 class="units-heading">UNITS OF STUDY</h3>
      <div class="level-band">Years 1 and 2: Diploma Level</div>
      <ul class="unit-list">
        <li>Working in industry 4.0</li>
        <li>Technical drawing and design</li>
        <li>Applied mathematics for engineers</li>
        <li>Electrical principles and safety</li>
        <li>Programmable logic controllers</li>
        <li>Sensors and data acquisition</li>
        <li>Network fundamentals for automation</li>
        <li>Mechanical systems and materials</li>
        <li>Workplace project and reporting</li>
      </ul>
      <div class="level-band">Years 3 and 4: Associate Degree Level</div>
      <ul class="unit-list">
        <li>Working in industry 4.0</li>
        <li>Engineering maths for industry 4.0</li>
        <li>CAD / CAM and 3D printing</li>
        <li>Introduction to robotics and computing</li>
        <li>Electrical systems</li>
        <li>Digital control programming</li>
        <li>Industrial control systems integration</li>
        <li>Cyber physical systems</li>
        <li>Advanced tools for industry 4.0</li>
        <li>Project management (Major Project)</li>
        <li>Advanced digital control systems</li>
        <li>Data and engineering analytics</li>
        <li>Cyber security and digital twin</li>
        <li>Distributed control in a smart factory</li>
        <li>Smart product design using industry 4.0</li>
      </ul>
    </div>
  </section>

</body>
</html>
```